An innovative software company needs a business card!

We need a business card design for our new innovative software company. Please use the details for the business card provided in business card details section. We will use the business card paper like: https://www.plavex.com/us/products/nfc/business-cards-plus.html Our company name: kelvora We have already a logo and colors to use in business cards too ,

Target Market(s)

App & Sofware Development

Industry/Entity Type

Software

Contact Information for Business Card

Lukas Brenner, BSc.
Owner and Creative Superhero

Adress:
Tulpenweg 37/4/1809
A - 1100, Wien

Tel: +43 (0) 676 921 35 60
Email: lukas.brenner@kelvora.at
Web: www.kelvora.at

Requirements
Must have
• - Use our logo
Nice to have
• It would be nice to have a nice picture on the backside. (About apps, software, technicals or funy stuff) - Use our colors as in business card (optional)

```html
<!DOCTYPE html>
<html lang="en">
<head>
<meta charset="utf-8">
<title>kelvora – business card</title>
<link rel="stylesheet" href="https://fonts.googleapis.com/css2?family=Montserrat:wght@400;500;700;800&display=swap">
<style>
  :root {
    --page: #2a2b2d;
    --card-black: #050505;
    --card-back-top: #1f2a33;
    --card-back-bottom: #12171c;
    --brand-blue: #1aa3d4;
    --brand-grey: #c9cbce;
    --text-white: #f2f4f5;
  }
  * { margin: 0; padding: 0; box-sizing: border-box; }
  html, body {
    width: 1200px; height: 900px; overflow: hidden;
    background: var(--page);
    font-family: "Montserrat", sans-serif;
  }
  .canvas {
    position: relative; width: 1200px; height: 900px;
  }
  .card {
    position: absolute; width: 600px; height: 343px;
    border-radius: 22px; overflow: hidden;
    box-shadow: 0 18px 40px rgba(0,0,0,0.45);
  }
  /* Back side */
  .card-back { left: 300px; top: 70px; }
  .back-artwork {
    position: absolute; inset: 0;
    background:
      radial-gradient(circle at 32% 62%, #2c3a46 0%, #1b242c 38%, transparent 60%),
      linear-gradient(135deg, var(--card-back-top), var(--card-back-bottom));
  }
  .back-brand {
    position: absolute; left: 0; right: 0; top: 120px;
    display: flex; justify-content: center; align-items: center; gap: 14px;
  }
  .brand-dot {
    width: 40px; height: 40px; border-radius: 50%;
    background: var(--brand-blue);
  }
  .back-brand .brand-name {
    font-weight: 800; font-size: 48px; color: var(--brand-blue);
    letter-spacing: 0.5px;
  }
  .back-url {
    position: absolute; left: 0; right: 0; bottom: 46px;
    text-align: center; font-size: 19px; font-weight: 400;
    color: var(--brand-blue); letter-spacing: 0.5px;
  }
  .back-url strong { color: var(--text-white); font-weight: 700; }

  /* Front side */
  .card-front { left: 300px; top: 480px; background: var(--card-black); }
  .front-brand {
    position: absolute; left: 44px; top: 132px;
    display: flex; align-items: center; gap: 14px;
  }
  .front-brand .brand-dot { width: 46px; height: 46px; }
  .front-brand .brand-name {
    font-weight: 800; font-size: 52px; color: var(--brand-blue);
    letter-spacing: 0.5px; line-height: 1;
  }
  .contact {
    position: absolute; left: 330px; top: 92px;
    color: var(--text-white); font-size: 13px; line-height: 1.5;
  }
  .contact-name {
    color: var(--brand-blue); font-weight: 800; font-size: 18px; line-height: 1.2;
  }
  .contact-title { margin-bottom: 2px; }
  .contact-lines { list-style: none; margin-top: 2px; }
  .contact-lines li { display: flex; align-items: center; gap: 8px; }
  .contact-lines svg { width: 10px; height: 10px; flex: none; }
  .contact-lines .web strong { color: var(--brand-blue); font-weight: 700; }
</style>
</head>
<body>
<main class="canvas">

  <section class="card card-back" aria-label="Card back">
    <div class="back-artwork" role="img" aria-label="Dark technology illustration with circular circuit rings and hexagon grid"></div>
    <div class="back-brand">
      <span class="brand-dot"></span>
      <span class="brand-name">kelvora</span>
    </div>
    <p class="back-url">www.<strong>kelvora</strong>.at</p>
  </section>

  <section class="card card-front" aria-label="Card front">
    <div class="front-brand">
      <span class="brand-dot"></span>
      <span class="brand-name">kelvora</span>
    </div>
    <div class="contact">
      <p class="contact-name">Lukas Brenner, BSc</p>
      <p class="contact-title">Owner and Creative Superhero</p>
      <p>Tulpenweg 37/4/1809</p>
      <p>A - 1100, Wien</p>
      <ul class="contact-lines">
        <li>
          <svg viewBox="0 0 10 10" aria-hidden="true"><path d="M2 1 L4 1 L4.6 3 L3.4 3.8 Q4.4 5.8 6.2 6.6 L7 5.4 L9 6 L9 8 Q5 9 1.5 5 Q0.5 3 2 1 Z" fill="var(--brand-blue)"/></svg>
          <span>+43 (0) 676 921 35 60</span>
        </li>
        <li class="web">
          <svg viewBox="0 0 10 10" aria-hidden="true"><circle cx="5" cy="5" r="4" fill="none" stroke="var(--brand-blue)" stroke-width="1.2"/><path d="M1 5 H9 M5 1 Q2.5 5 5 9 Q7.5 5 5 1" fill="none" stroke="var(--brand-blue)" stroke-width="0.9"/></svg>
          <span>www.<strong>kelvora</strong>.at</span>
        </li>
        <li>
          <svg viewBox="0 0 10 10" aria-hidden="true"><rect x="0.8" y="2" width="8.4" height="6" fill="none" stroke="var(--brand-blue)" stroke-width="1.2"/><path d="M0.8 2 L5 5.4 L9.2 2" fill="none" stroke="var(--brand-blue)" stroke-width="1"/></svg>
          <span>lukas.brenner@kelvora.at</span>
        </li>
      </ul>
    </div>
  </section>

</main>
</body>
</html>
```